Very Simple/Minimal Business Card Design Project

The company operates in the industrial maritime infrastructure sector in Brazil. You can find more information on our website www.navelquor.com.br WE NEED TO LOOK POWERFUL AND SERIOUS
I have attached a copy of the old cards. We would like something more professional / industrial / sexy that also includes the position.

The card can be double sided or not. We would like you to propose as many options.

Thank you
Updates

Many thanks, do let me know if you have any questions. I am under a lot of time pressure to try and have them printed over the next days or so.

Please could you use the following information

for the address: Rua Tapiraçu, 418 - Centro, Rio de Janeiro, 20135-070, Brasil

for the mobile: +55 21 8372 9041
for the landline: +55 21 4067 3859

and position:  Diretor Geral

Thakn you

Target Market(s)

Shipowners, bankers, industrial companies

Industry/Entity Type

Industrial

Requirements
Must have
• POWERFUL
SERIOUS
SOLID
BIG CORPORATION

```html
<!DOCTYPE html>
<html lang="pt-BR">
<head>
<meta charset="utf-8">
<title>Navelquor – Business Card</title>
<link href="https://fonts.googleapis.com/css2?family=Source+Sans+3:wght@300;700&display=swap" rel="stylesheet">
<style>
  :root {
    --navy: #002776;
    --green: #009b3a;
    --white: #ffffff;
    --white-soft: rgba(255, 255, 255, 0.82);
    --stage-edge: #e2e2e2;
    --stage-mid: #f5f5f5;
    --accent-faint: #02426a;
  }
  * { margin: 0; padding: 0; box-sizing: border-box; }
  html, body {
    width: 978px;
    height: 1200px;
    overflow: hidden;
  }
  body {
    position: relative;
    background: linear-gradient(to bottom, var(--stage-edge) 0%, var(--stage-mid) 50%, var(--stage-edge) 100%);
    font-family: "Source Sans 3", "Myriad Pro", sans-serif;
    color: var(--white);
  }
  .card {
    position: absolute;
    left: 71px;
    width: 836px;
    height: 477px;
    background: var(--navy);
    border: 8px solid var(--green);
    overflow: hidden;
  }
  .card--front { top: 94px; }
  .card--back  { top: 640px; }

  /* Front: brand lockup */
  .brand {
    position: absolute;
    left: 113px;
    top: 165px;
    display: flex;
    align-items: center;
    gap: 17px;
  }
  .brand__square {
    width: 119px;
    height: 119px;
    background: var(--green);
    border-radius: 10px;
  }
  .brand__name {
    font-weight: 700;
    font-size: 84px;
    letter-spacing: 1px;
    line-height: 1;
    color: var(--white);
  }

  /* Back */
  .back__accent {
    position: absolute;
    left: 540px;
    top: 10px;
    width: 200px;
    height: 200px;
    background: var(--accent-faint);
    border-radius: 14px;
    transform: rotate(-24deg);
  }
  .holder {
    position: absolute;
    left: 0;
    right: 0;
    top: 214px;
    padding-left: 24px;
    text-align: center;
  }
  .holder__name {
    font-weight: 300;
    font-size: 46px;
    letter-spacing: 1.5px;
    line-height: 1;
  }
  .holder__role {
    margin-top: 12px;
    font-weight: 300;
    font-size: 22px;
    letter-spacing: 2px;
    line-height: 1;
    color: var(--white-soft);
  }
  .contact {
    position: absolute;
    bottom: 4px;
    font-weight: 300;
    font-size: 23px;
    line-height: 30px;
    font-style: normal;
  }
  .contact--left  { left: 18px; }
  .contact--right { right: 18px; text-align: right; }
</style>
</head>
<body>

  <section class="card card--front">
    <div class="brand">
      <div class="brand__square"></div>
      <div class="brand__name">NAVELQUOR</div>
    </div>
  </section>

  <section class="card card--back">
    <div class="back__accent"></div>

    <div class="holder">
      <h1 class="holder__name">Rafael&nbsp;&nbsp;Monteiro</h1>
      <p class="holder__role">Diretor Geral</p>
    </div>

    <div class="contact contact--left">
      <p>T: +55 21 4067 3859</p>
      <p>M: +55 21 8372 9041</p>
      <p>rafael@navelquor.com.br</p>
      <p>www.navelquor.com.br</p>
    </div>

    <address class="contact contact--right">
      <p>R.Tapiraçu 418</p>
      <p>Centro</p>
      <p>CEP 20135-070</p>
      <p>Rio de Janeiro</p>
    </address>
  </section>

</body>
</html>
```